Equipment Finance Specialist I work with companies who need the funds to buy their equipment

I would like a business card that stands out on the shelves. I want to be able to hand it to someone and say WOW. This card should have my logo.
You can put color into it I am very open on design and color

What my company does is we deal with dealerships that sell equipment such as Dump Trucks garbage trucks tractors trailers. Customers get referred to us and depending on their time in business we will ask for the following items

Companies that have been in business for more than two years we have a credit application program up to 250K . With this program we need the following items Credit application filled out(which is what I would like to be able for the customer to click on my website to get.) as well as three current month bank statements.

Deals over 250k we will need the following items

2 years business tax returns
2 years personal tax returns
Profit & Loss statement
Personal Financial Statement

what we do
100% FINANCING
SEASONAL PAYMENTS
LOAN BALLOON PAYMENTS
TRAC LEASING
LOW-INTEREST REFINANCING RATES
DEBT CONSOLIDATION

We specialize in creative financing solutions and offer a variety of reliable, flexible and expandable lending choices.

Target Market(s)

Trucking Companies

Industry/Entity Type

Trucking Company

Contact Information for Business Card

* $250,000 Application only Program
* Loans from $30,000 to 5,000,000
* Competitive Interest Rates

Font styles to use
Serif
Sans Serif

Colors

Designer to choose colors to be used in the design.

Requirements
Must have
• On the back of the card.
• * $250,000 Application only Program
• * Loans from $30,000 to 5,000,000
• My name, email, website. address
• * Competitive Interest Rates
• * 100% Financing
Nice to have
• I want my logo to pop on the card
• My logo is the great one I would like to use
Should not have
• I am up for your creativity as well

```html
<!DOCTYPE html>
<html lang="en">
<head>
<meta charset="utf-8">
<title>Ironroad Finance – Business Card</title>
<link href="https://fonts.googleapis.com/css2?family=Jura:wght@400;600;700&display=swap" rel="stylesheet">
<style>
  :root {
    --backdrop: #3a3a3a;
    --card: #272727;
    --red: #e11d2e;
    --white: #f2f2f2;
    --silver: #c9c9c9;
  }
  * { box-sizing: border-box; margin: 0; padding: 0; }
  html, body {
    width: 1200px; height: 900px; overflow: hidden;
    background: var(--backdrop);
    font-family: "Jura", sans-serif;
  }
  .canvas { position: relative; width: 1200px; height: 900px; }
  .card {
    position: absolute; left: 230px; width: 740px; height: 423px;
    background: var(--card);
    box-shadow: 0 10px 30px rgba(0,0,0,.45);
    overflow: hidden;
  }
  .card--front { top: 24px; }
  .card--back { top: 463px; }
  .card__band {
    position: absolute; left: 0; right: 0; bottom: 0; height: 16px;
    background: var(--red);
  }

  /* front */
  .brand {
    position: absolute; left: 44px; top: 40px;
    display: flex; align-items: center; gap: 16px;
  }
  .brand__dot {
    width: 64px; height: 64px; border-radius: 50%;
    background: var(--silver);
  }
  .brand__name {
    color: var(--silver); font-weight: 700; font-size: 42px;
    letter-spacing: 1px; line-height: 1; text-transform: uppercase;
  }
  .features {
    position: absolute; right: 40px; bottom: 46px;
    list-style: none; text-align: right;
    color: var(--white); font-size: 17px; line-height: 1.2;
    letter-spacing: .5px;
  }

  /* back */
  .emblem {
    position: absolute; left: 40px; top: 96px; width: 236px; height: 200px;
    display: flex; flex-direction: column; align-items: center; justify-content: center; gap: 16px;
  }
  .emblem__dot {
    width: 110px; height: 110px; border-radius: 50%;
    background: var(--silver);
  }
  .emblem__name {
    color: var(--silver); font-weight: 700; font-size: 22px;
    text-transform: uppercase; letter-spacing: 1px;
  }
  .divider {
    position: absolute; left: 318px; top: 22px; width: 3px; height: 280px;
    background: var(--red);
  }
  .contact { position: absolute; left: 352px; top: 26px; right: 20px; }
  .contact__name {
    font-size: 30px; font-weight: 700; color: var(--white); letter-spacing: 1px;
  }
  .contact__name span { color: var(--red); }
  .contact__role { font-size: 14px; font-weight: 700; color: var(--white); margin-top: 2px; }
  .contact__address {
    font-size: 19px; color: var(--red); line-height: 1.2; margin-top: 12px; letter-spacing: .5px;
  }
  .contact__list { list-style: none; margin-top: 16px; }
  .contact__item {
    display: flex; align-items: center; gap: 22px;
    font-size: 20px; color: var(--white); height: 40px; letter-spacing: .5px;
  }
  .contact__icon { width: 22px; height: 22px; fill: var(--red); flex: none; }
</style>
</head>
<body>
<main class="canvas">

  <section class="card card--front">
    <div class="brand">
      <span class="brand__dot"></span>
      <span class="brand__name">Ironroad Finance</span>
    </div>
    <ul class="features">
      <li>*$250,000 Application only Program</li>
      <li>*Loans from $30,000 to 5,000,000</li>
      <li>*Competitive Interest Rates</li>
      <li>*100% Financing</li>
    </ul>
    <div class="card__band"></div>
  </section>

  <section class="card card--back">
    <div class="emblem">
      <span class="emblem__dot"></span>
      <span class="emblem__name">Ironroad Finance</span>
    </div>
    <div class="divider"></div>
    <div class="contact">
      <h1 class="contact__name">Marcus <span>Hale</span></h1>
      <p class="contact__role">Founder | CEO</p>
      <p class="contact__address">48 Kestrel Lane,<br>Northvale, Auckland 1041, NZ</p>
      <ul class="contact__list">
        <li class="contact__item">
          <svg class="contact__icon" viewBox="0 0 24 24"><path d="M6.6 10.8a15 15 0 0 0 6.6 6.6l2.2-2.2a1 1 0 0 1 1-.25 11.4 11.4 0 0 0 3.6.57 1 1 0 0 1 1 1V20a1 1 0 0 1-1 1A17 17 0 0 1 3 4a1 1 0 0 1 1-1h3.5a1 1 0 0 1 1 1c0 1.25.2 2.45.57 3.57a1 1 0 0 1-.25 1z"/></svg>
          +64 (0)9555 0142
        </li>
        <li class="contact__item">
          <svg class="contact__icon" viewBox="0 0 24 24"><path d="M2 8c3-4 17-4 20 0v2h-5V8H7v2H2z"/><path d="M5 12h14l2 8H3z"/><circle cx="12" cy="16" r="2" fill="#272727"/></svg>
          021 555 318
        </li>
        <li class="contact__item">
          <svg class="contact__icon" viewBox="0 0 24 24"><path d="M2 5h20v14H2z"/><path d="M2 5l10 8 10-8" fill="none" stroke="#272727" stroke-width="1.6"/></svg>
          info@ironroadfinance.com
        </li>
        <li class="contact__item">
          <svg class="contact__icon" viewBox="0 0 24 24"><circle cx="12" cy="12" r="10"/><path d="M2 12h20M12 2c3 3 3 17 0 20M12 2c-3 3-3 17 0 20M4 7h16M4 17h16" fill="none" stroke="#272727" stroke-width="1.3"/></svg>
          www.ironroadfinance.com
        </li>
      </ul>
    </div>
    <div class="card__band"></div>
  </section>

</main>
</body>
</html>
```